Business card design needed

partition walls
suspended ceilings
bulkheads
shops
office fitouts
compressed sheeting

main colour aqua blue with silver and white writing

k.r.m plastering (vic) pty.ltd

noel carrow
M:0400712864 E:krmplastering@mailvane.com
ABN: 64 203 917 482
ACN: 271 604 815

```html
<!DOCTYPE html>
<html lang="en">
<head>
<meta charset="utf-8">
<title>KRM Plastering — Business Card</title>
<link rel="stylesheet" href="https://fonts.googleapis.com/css2?family=Arimo:wght@400&family=Archivo:wght@800&display=swap">
<style>
  :root {
    --aqua: #1cbfd1;
    --aqua-deep: #13a9ba;
    --aqua-pale: #5fd3e0;
    --card-body: #ececec;
    --ink: #0a0a0a;
    --white: #f4f4f4;
    --silver: #a9a9a9;
    --page: #ffffff;
  }
  * { box-sizing: border-box; margin: 0; padding: 0; }
  html, body {
    width: 1200px; height: 1000px; overflow: hidden;
    background: var(--page);
  }
  .stage {
    width: 1200px; height: 1000px;
    display: flex; align-items: center; justify-content: center;
  }
  .business-card {
    position: relative;
    width: 1100px; height: 640px;
    background: var(--card-body);
    overflow: hidden;
    font-family: "Arimo", Arial, sans-serif;
    box-shadow: 0 2px 10px rgba(0,0,0,0.18);
  }
  .header-band {
    position: absolute; left: 0; top: 0;
    width: 1100px; height: 185px;
  }
  .company-name {
    position: absolute; left: 0; right: 0; top: 58px;
    text-align: center;
    font-family: "Arimo", Arial, sans-serif;
    font-weight: 400; font-size: 60px; letter-spacing: 0.5px;
    color: var(--white); line-height: 1;
  }
  .company-suffix {
    position: absolute; left: 0; right: 0; top: 134px;
    text-align: center;
    font-family: "Arimo", Arial, sans-serif;
    font-weight: 400; font-size: 30px; letter-spacing: 1px;
    color: var(--white); line-height: 1;
  }
  .contact-block {
    position: absolute; left: 245px; top: 250px;
  }
  .person-name {
    font-family: "Archivo", "Arimo", sans-serif;
    font-weight: 800; font-size: 48px; letter-spacing: 1px;
    color: var(--ink); line-height: 1;
    margin-bottom: 22px;
  }
  .contact-line {
    display: flex; align-items: center; gap: 26px;
    font-size: 32px; color: var(--ink);
    margin-bottom: 20px;
  }
  .contact-icon { width: 46px; height: 46px; flex: none; }
  .registration {
    position: absolute; left: 0; right: 0; top: 500px;
    text-align: center;
    font-size: 21px; color: var(--silver); letter-spacing: 0.5px;
  }
  .registration .divider { margin: 0 20px; }
  .services-band {
    position: absolute; left: 0; top: 530px;
    width: 1100px; height: 80px;
    background: var(--ink);
    color: var(--white);
    font-size: 24px; line-height: 1.2;
    text-align: center;
    padding-top: 10px;
  }
  .service-dot { color: var(--aqua); margin: 0 12px; }
</style>
</head>
<body>
<main class="stage">
  <article class="business-card">
    <svg class="header-band" viewBox="0 0 1100 185" aria-hidden="true">
      <rect width="1100" height="185" fill="var(--aqua-deep)"/>
      <polygon points="0,0 1100,185 0,185" fill="var(--aqua)"/>
      <polygon points="0,0 300,0 0,14" fill="var(--aqua-pale)"/>
    </svg>
    <h1 class="company-name">KRM Plastering</h1>
    <p class="company-suffix">(Vic) Pty. Ltd.</p>

    <section class="contact-block">
      <h2 class="person-name">NOEL CARROW</h2>
      <p class="contact-line">
        <svg class="contact-icon" viewBox="0 0 46 46" aria-label="Phone">
          <circle cx="23" cy="23" r="23" fill="var(--aqua)"/>
          <path d="M16 12c2-1 3 0 4 2l1 4c0 1-1 2-2 2 1 3 3 6 6 7 0-1 1-2 2-2l4 1c2 1 3 2 2 4-1 2-3 3-5 3-8-2-14-9-15-16 0-2 1-4 3-5z" fill="var(--white)"/>
        </svg>
        <span class="phone">0400 712 864</span>
      </p>
      <p class="contact-line">
        <svg class="contact-icon" viewBox="0 0 46 46" aria-label="Email">
          <circle cx="23" cy="23" r="23" fill="var(--aqua)"/>
          <rect x="11" y="15" width="24" height="16" fill="var(--white)"/>
          <path d="M11 15l12 9 12-9" fill="none" stroke="var(--aqua)" stroke-width="2"/>
        </svg>
        <span class="email">krmplastering@mailvane.com</span>
      </p>
    </section>

    <p class="registration">ABN: 64 203 917 482<span class="divider">|</span>ACN: 271 604 815</p>

    <footer class="services-band">
      <div>PARTITION WALLS<span class="service-dot">•</span>SUSPENDED CEILINGS<span class="service-dot">•</span>BULKHEADS</div>
      <div>SHOPS<span class="service-dot">•</span>OFFICE FITOUTS<span class="service-dot">•</span>COMPRESSED SHEETING</div>
    </footer>
  </article>
</main>
</body>
</html>
```